Social Media Graphics - Copperfield Loop

Create 6-7 individual social media graphics (square size) to encourage folks to join our online course, using either of the text below (only one set of text per graphic:

The Lantern Ridge Method
How to Create a 7-Figure Business From Scratch
Sign Up Today!

Or

The Lantern Ridge Method
Fast-track Your Way to a Multi-Million Business!
Sign Up Today!

For the color scheme of the graphics, use 1 or 2 colors in the color palette attached; or use any colors that look nice with their outfits; AVOID using red, white and blue altogether because it will look like an Independence Day (4th of July) graphic and we don’t want that; make sure the graphics appeal to both men and women

Make sure each graphic contains 1 of the 2 pics attached; and make sure one of the graphics is all TEXT only.

Target Market(s)

men and women looking to make more money

Industry/Entity Type

entrepreneurship

Requirements
Must have
• see the text document attached
Nice to have
• We are open to a nice color design; the color palette colors are not required, especially we don't want red, white and blue used together
Should not have
• AVOID using red, white and blue altogether because it will look like an Independence Day (4th of July) graphic and we dont want that

```html
<!DOCTYPE html>
<html lang="en">
<head>
<meta charset="utf-8">
<title>The Lantern Ridge Method — Social Graphics</title>
<link rel="stylesheet" href="https://fonts.googleapis.com/css2?family=Montserrat:ital,wght@0,800;0,900;1,900&family=Oswald:wght@600&display=swap">
<style>
  :root {
    --sheet: #000000;
    --royal: #0b3fb0;
    --royal-deep: #06297a;
    --royal-light: #1f5fd6;
    --navy: #0b2f86;
    --gold: #f2b016;
    --gold-text: #e0a614;
    --white: #ffffff;
    --pink: #e8185c;
    --pink-soft: #f0587f;
    --crimson: #ee0f3f;
    --cocoa: #2e1b18;
    --cocoa-deep: #1e100e;
    --title-font: "Montserrat", "Arial Black", sans-serif;
    --button-font: "Oswald", "Arial Narrow", sans-serif;
  }
  * { margin: 0; padding: 0; box-sizing: border-box; }
  html, body { width: 1200px; height: 2402px; overflow: hidden; background: var(--sheet); }
  .sheet { position: relative; width: 1200px; height: 2402px; }

  .tile { position: absolute; width: 578px; height: 578px; overflow: hidden; }
  .col-1 { left: 17px; } .col-2 { left: 606px; }
  .row-1 { top: 28px; } .row-2 { top: 618px; } .row-3 { top: 1209px; } .row-4 { top: 1798px; }

  .layer { position: absolute; inset: 0; }
  .abs { position: absolute; }

  .title {
    position: absolute; left: 0; right: 0; text-align: center;
    font-family: var(--title-font); font-weight: 900; text-transform: uppercase;
    letter-spacing: -1.5px; line-height: 0.98; white-space: nowrap;
  }
  .title .line-1 { display: block; font-size: 57px; }
  .title .line-2 { display: block; font-size: 61px; }

  .subtitle {
    position: absolute; left: 20px; right: 20px; text-align: center;
    font-family: var(--title-font); font-weight: 900; text-transform: uppercase;
    font-size: 23px; line-height: 1.15; letter-spacing: 0.5px;
  }

  .pitch {
    position: absolute; text-align: center;
    font-family: var(--title-font); font-weight: 900; font-style: italic;
    text-transform: uppercase; font-size: 31px; line-height: 1.2; color: var(--white);
    text-shadow: 0 2px 6px rgba(0,0,0,0.35);
  }
  .pitch .small { font-size: 21px; }
  .pitch--plain { font-style: normal; font-size: 30px; }

  .signup {
    position: absolute; height: 46px; border-radius: 23px; border: 3px solid;
    font-family: var(--button-font); font-weight: 600; text-transform: uppercase;
    font-size: 29px; line-height: 38px; text-align: center; color: var(--white);
    letter-spacing: -0.5px;
  }

  .photo { position: absolute; }

  /* Blue photo tile */
  .tile--blue-photo { background: linear-gradient(160deg, var(--royal-light), var(--royal) 45%, var(--royal-deep)); }
  .tile--blue-photo .title { top: 20px; color: var(--white); text-shadow: 0 3px 8px rgba(0,0,0,0.35); }
  .tile--blue-photo .accent { color: var(--gold); }
  .tile--blue-photo .photo { left: 0; top: 168px; width: 360px; height: 410px;
    background: linear-gradient(180deg, #3a2a24 0%, #1d1a22 55%, #1b2c5c 100%); }
  .tile--blue-photo .pitch { left: 372px; width: 206px; top: 252px; }
  .tile--blue-photo .signup { left: 373px; top: 520px; width: 191px; background: var(--royal-deep); border-color: var(--gold); }

  /* Text-only tiles */
  .tile--text .title { top: 168px; }
  .tile--text .subtitle { top: 328px; }
  .tile--text .signup { left: 193px; top: 396px; width: 193px; }

  .tile--blue-text { background: var(--royal); }
  .tile--blue-text .title { color: var(--navy); }
  .tile--blue-text .accent { color: var(--gold-text); }
  .tile--blue-text .subtitle { color: var(--gold-text); }
  .tile--blue-text .signup { background: var(--navy); border-color: var(--gold); }

  .tile--pink-text { background: var(--pink); }
  .tile--pink-text .title { color: var(--crimson); }
  .tile--pink-text .accent { color: var(--cocoa); }
  .tile--pink-text .subtitle { color: var(--cocoa); }
  .tile--pink-text .signup { background: var(--cocoa); border-color: var(--crimson); }

  /* Red photo tile */
  .tile--red-photo { background: linear-gradient(180deg, #fbeeee 0%, #ff6a6a 22%, #e42a2a 50%, #9a1f1a 100%); }
  .tile--red-photo .title { top: 18px; color: var(--crimson);
    text-shadow: -2px -2px 0 var(--white), 2px -2px 0 var(--white), -2px 2px 0 var(--white), 2px 2px 0 var(--white), 0 4px 8px rgba(0,0,0,0.3); }
  .tile--red-photo .photo { left: 185px; top: 170px; width: 393px; height: 408px;
    background: linear-gradient(180deg, #3a231d 0%, #6a3a2c 35%, #e8305a 70%, #1c1414 100%); }
  .tile--red-photo .pitch { left: 4px; width: 190px; top: 233px; }
  .tile--red-photo .signup { left: 191px; top: 519px; width: 193px; background: rgba(60,20,18,0.55); border-color: #f2a0a8; }
</style>
</head>
<body>
<main class="sheet">

  <!-- Row 1 -->
  <section class="tile tile--blue-photo col-1 row-1">
    <svg class="layer" viewBox="0 0 578 578" aria-hidden="true"><polygon points="578,157 578,176 230,300 205,296" fill="var(--gold)"/></svg>
    <h2 class="title"><span class="line-1">The <span class="accent">Lantern</span></span><span class="line-2">Ridge Method</span></h2>
    <div class="photo" role="img" aria-label="Photo of the two course hosts standing with arms crossed"></div>
    <p class="pitch">Fast<br>Track<br><span class="small">Your Way</span><br>To A<br>Multi<br>Million<br><span class="small">Business!</span></p>
    <div class="signup">Sign Up Today!</div>
  </section>

  <section class="tile tile--text tile--blue-text col-2 row-1">
    <div class="layer" role="img" aria-label="Blue-tinted city street backdrop"></div>
    <svg class="layer" viewBox="0 0 578 578" aria-hidden="true"><polygon points="0,146 578,81 578,471 0,529" fill="var(--white)"/></svg>
    <h2 class="title"><span class="line-1">The <span class="accent">Lantern</span></span><span class="line-2">Ridge Method</span></h2>
    <p class="subtitle">Fast-track your way to a<br>multi-million business!</p>
    <div class="signup">Sign Up Today!</div>
  </section>

  <!-- Row 2 -->
  <section class="tile tile--text tile--pink-text col-1 row-2">
    <div class="layer" role="img" aria-label="Pink-tinted city street backdrop"></div>
    <svg class="layer" viewBox="0 0 578 578" aria-hidden="true"><polygon points="0,141 578,79 578,467 0,528" fill="var(--white)"/></svg>
    <h2 class="title"><span class="line-1">The <span class="accent">Lantern</span></span><span class="line-2">Ridge Method</span></h2>
    <p class="subtitle">Fast-track your way to a<br>multi-million business!</p>
    <div class="signup">Sign Up Today!</div>
  </section>

  <section class="tile tile--red-photo col-2 row-2">
    <div class="layer" role="img" aria-label="Red-tinted city street backdrop"></div>
    <svg class="layer" viewBox="0 0 578 578" aria-hidden="true"><polygon points="0,250 230,470 0,578" fill="var(--cocoa-deep)" opacity="0.7"/><polygon points="0,578 578,330 578,578" fill="var(--crimson)" opacity="0.85"/></svg>
    <h2 class="title"><span class="line-1">The Lantern</span><span class="line-2">Ridge Method</span></h2>
    <div class="photo" role="img" aria-label="Photo of the two course hosts smiling, arms crossed"></div>
    <p class="pitch">Fast<br>Track<br><span class="small">Your Way</span><br>To A<br>Multi<br>Million<br><span class="small">Business!</span></p>
    <div class="signup">Sign Up Today!</div>
  </section>

  <!-- Row 3 -->
  <section class="tile tile--blue-photo col-1 row-3">
    <svg class="layer" viewBox="0 0 578 578" aria-hidden="true"><polygon points="578,157 578,176 230,300 205,296" fill="var(--gold)"/></svg>
    <h2 class="title"><span class="line-1">The <span class="accent">Lantern</span></span><span class="line-2">Ridge Method</span></h2>
    <div class="photo" role="img" aria-label="Photo of the two course hosts standing with arms crossed"></div>
    <p class="pitch pitch--plain" style="top:262px">How To<br>Create A<br>7-Figure<br>Business<br>From<br>Scratch</p>
    <div class="signup">Sign Up Today!</div>
  </section>

  <section class="tile tile--text tile--blue-text col-2 row-3">
    <div class="layer" role="img" aria-label="Blue-tinted city street backdrop"></div>
    <svg class="layer" viewBox="0 0 578 578" aria-hidden="true"><polygon points="0,146 578,81 578,471 0,529" fill="var(--white)"/></svg>
    <h2 class="title"><span class="line-1">The <span class="accent">Lantern</span></span><span class="line-2">Ridge Method</span></h2>
    <p class="subtitle">How to create a 7-figure business<br>from scratch</p>
    <div class="signup">Sign Up Today!</div>
  </section>

  <!-- Row 4 -->
  <section class="tile tile--text tile--pink-text col-1 row-4">
    <div class="layer" role="img" aria-label="Pink-tinted city street backdrop"></div>
    <svg class="layer" viewBox="0 0 578 578" aria-hidden="true"><polygon points="0,141 578,79 578,467 0,528" fill="var(--white)"/></svg>
    <h2 class="title"><span class="line-1">The <span class="accent">Lantern</span></span><span class="line-2">Ridge Method</span></h2>
    <p class="subtitle">How to create a 7-figure business<br>from scratch</p>
    <div class="signup">Sign Up Today!</div>
  </section>

  <section class="tile tile--red-photo col-2 row-4">
    <div class="layer" role="img" aria-label="Red-tinted city street backdrop"></div>
    <svg class="layer" viewBox="0 0 578 578" aria-hidden="true"><polygon points="0,250 230,470 0,578" fill="var(--cocoa-deep)" opacity="0.7"/><polygon points="0,578 578,330 578,578" fill="var(--crimson)" opacity="0.85"/></svg>
    <h2 class="title"><span class="line-1">The Lantern</span><span class="line-2">Ridge Method</span></h2>
    <div class="photo" role="img" aria-label="Photo of the two course hosts smiling, arms crossed"></div>
    <p class="pitch" style="top:238px">How To<br>Create A<br>7-Figure<br>Business<br>From<br>Scratch</p>
    <div class="signup">Sign Up Today!</div>
  </section>

</main>
</body>
</html>
```